Groovy little Insurance brokerage needs a new look

We have a new logo, but need to work out how to make it work for us!
We are a small insurance broking firm (three staff with different focus and styles), with lots of energy, experience and enthusiasm. A focus on both commercial and domestic market. We would like our cards to show a fresh look - while veering away from the 'run of the mill' insurance industry (often dull) approach.
Updates

Thanks to all for your concepts.

Had some great ideas come back, now just the process of picking which one is going to work best for us...
Will advise when we've had an opportunity to review.

Thanks!
From the team at
Kestrel Dunmore Insurance Brokers

Thanks SO much to all of your for your great designs.  Now just a process of sorting out the favorites.  If yours is eliminated, just want to say a collective thank you for your efforts!

Industry/Entity Type

Business

```html
<!DOCTYPE html>
<html lang="en">
<head>
<meta charset="utf-8">
<title>Kestrel Dunmore Insurance Brokers – Business Card</title>
<link rel="stylesheet" href="https://fonts.googleapis.com/css2?family=Arimo:wght@400;700&family=Open+Sans:wght@400;600&display=swap">
<style>
  :root {
    --stripe-1: #001f24;
    --stripe-2: #00434f;
    --stripe-3: #006676;
    --stripe-4: #007f91;
    --stripe-5: #00b5d1;
    --stripe-6: #008599;
    --stripe-7: #006a7a;
    --paper: #ececec;
    --paper-light: #f6f6f6;
    --charcoal: #231f20;
    --teal: #12abc6;
    --teal-pale: #aed9e4;
    --ink: #1c1a1b;
    --ink-teal: #0b3b45;
    --white: #ffffff;
    --gap: #d8d8d8;
  }
  html, body {
    margin: 0;
    padding: 0;
    width: 1200px;
    height: 734px;
    overflow: hidden;
    background: var(--white);
  }
  .card {
    position: relative;
    width: 1200px;
    height: 734px;
    overflow: hidden;
    font-family: "Arimo", Arial, sans-serif;
    background: var(--gap);
  }
  .stripe-bar {
    position: absolute;
    top: 0; left: 0;
    width: 1200px; height: 73px;
    display: flex;
  }
  .stripe-bar span { flex: 1; }
  .stripe-bar span:nth-child(1), .stripe-bar span:nth-child(9) { background: var(--stripe-1); }
  .stripe-bar span:nth-child(2), .stripe-bar span:nth-child(8) { background: var(--stripe-2); }
  .stripe-bar span:nth-child(3) { background: var(--stripe-3); }
  .stripe-bar span:nth-child(4) { background: var(--stripe-4); }
  .stripe-bar span:nth-child(5) { background: var(--stripe-5); }
  .stripe-bar span:nth-child(6) { background: var(--stripe-6); }
  .stripe-bar span:nth-child(7) { background: var(--stripe-7); }

  .brand-band {
    position: absolute;
    top: 73px; left: 0;
    width: 1200px; height: 232px;
    background: radial-gradient(ellipse at 50% 40%, var(--paper-light), var(--paper));
  }
  .brand {
    position: absolute;
    left: 604px; top: 51px;
    display: flex;
    align-items: center;
    gap: 22px;
  }
  .brand-mark {
    width: 134px; height: 134px;
    background: var(--teal);
  }
  .brand-name {
    margin: 0;
    color: var(--ink);
    font-family: "Arimo", Arial, sans-serif;
    font-weight: 400;
    font-size: 40px;
    line-height: 1.2;
  }

  .name-band {
    position: absolute;
    top: 305px; left: 0;
    width: 1200px; height: 149px;
    background: var(--charcoal);
    color: var(--white);
    font-family: "Open Sans", Arial, sans-serif;
  }
  .person-name {
    position: absolute;
    left: 62px; top: 24px;
    margin: 0;
    font-size: 57px;
    font-weight: 400;
    line-height: 1.1;
  }
  .person-role {
    position: absolute;
    left: 65px; top: 83px;
    margin: 0;
    font-size: 27px;
    font-weight: 600;
  }

  .contact-panel {
    position: absolute;
    top: 459px; left: 0;
    width: 489px; height: 275px;
    background: var(--teal);
  }
  .contact-list {
    list-style: none;
    margin: 0;
    padding: 0;
    position: absolute;
    left: 64px; top: 30px;
    color: var(--ink-teal);
    font-size: 27px;
    line-height: 34.3px;
  }
  .contact-list li {
    display: flex;
    align-items: flex-start;
  }
  .contact-list svg {
    width: 32px; height: 32px;
    margin-right: 12px;
    flex: none;
    fill: none;
    stroke: var(--ink-teal);
    stroke-width: 1.8;
  }
  .contact-list .no-icon { padding-left: 44px; }

  .about-panel {
    position: absolute;
    top: 459px; left: 496px;
    width: 704px; height: 275px;
    background: var(--teal-pale);
  }
  .about-text {
    position: absolute;
    right: 46px; top: 72px;
    margin: 0;
    text-align: right;
    color: var(--ink);
    font-size: 26px;
    line-height: 34.6px;
  }
</style>
</head>
<body>
<div class="card">
  <div class="stripe-bar" aria-hidden="true">
    <span></span><span></span><span></span><span></span><span></span><span></span><span></span><span></span><span></span>
  </div>

  <header class="brand-band">
    <div class="brand">
      <div class="brand-mark" aria-hidden="true"></div>
      <p class="brand-name">Kestrel Dunmore<br>Insurance Brokers</p>
    </div>
  </header>

  <section class="name-band">
    <h1 class="person-name">Corin Vale</h1>
    <p class="person-role">Marketing Manager</p>
  </section>

  <section class="contact-panel">
    <ul class="contact-list">
      <li>
        <svg viewBox="0 0 32 32" aria-hidden="true"><path d="M3 15 L16 5 L29 15"/><path d="M7 12 V28 H25 V12"/><rect x="13" y="19" width="6" height="9"/><rect x="9" y="15" width="4" height="4"/><rect x="20" y="15" width="4" height="4"/></svg>
        <span>418 Harbour Lane</span>
      </li>
      <li class="no-icon">Port Avery 60218</li>
      <li>
        <svg viewBox="0 0 32 32" aria-hidden="true"><path d="M4 11 C4 5 28 5 28 11 L24 13 L21 10 H11 L8 13 Z"/><rect x="7" y="15" width="18" height="13" rx="2"/><circle cx="16" cy="21.5" r="3.5"/></svg>
        <span>+(000) 555 01942</span>
      </li>
      <li>
        <svg viewBox="0 0 32 32" aria-hidden="true"><rect x="6" y="3" width="20" height="27" rx="2"/><rect x="9" y="6" width="14" height="12"/><path d="M9 22 H23 M9 26 H23 M13.5 20 V29 M18.5 20 V29"/></svg>
        <span>+ (000) 555 817 304</span>
      </li>
      <li>
        <svg viewBox="0 0 32 32" aria-hidden="true"><rect x="3" y="8" width="26" height="17"/><path d="M3 8 L16 18 L29 8 M3 25 L12 15 M29 25 L20 15"/></svg>
        <span>corin@kdib.com</span>
      </li>
      <li>
        <svg viewBox="0 0 32 32" aria-hidden="true"><circle cx="16" cy="16" r="13"/><ellipse cx="16" cy="16" rx="6" ry="13"/><path d="M3 16 H29 M5 9 H27 M5 23 H27 M16 3 V29"/></svg>
        <span>www.kdib.com</span>
      </li>
    </ul>
  </section>

  <section class="about-panel">
    <p class="about-text">
      We are a small insurance broking firm<br>
      (three staff with different focus and styles),<br>
      with lots of energy,<br>
      experience and enthusiasm
    </p>
  </section>
</div>
</body>
</html>
```